(Wix) Website Design Tweaks

The site: www.MarbleFinchCo.com
(The coding must be done within Wix. I will create a duplicate website so you can gain access and begin editing.)

My website contains my preferred text and images - but it needs to look more professional. My business focuses on "Corporate Messaging" and "Marketing Communications", so the website needs to look professional, but not too corporate. My clients range from very big companies to technology startups - the look and feel should be uncluttered, professional, and modern.

I want someone to review the pages, and make changes / suggestions focused on:
1) Fonts
2) Colors
3) Layout

If you have ideas for adding additional graphics, that's fine, but they should be consistent with what I already have . . . unless you think some / all of my images need to be changed.

My site is very, very small, and only contains 5 (very short) pages. There are no sub-pages. (One page is the contact page, with almost nothing except form fields.)

If you do a good job with my site, I may be able to provide you with additional work - many of my clients need website design tweaks, after I provide the verbiage.

```html
<!DOCTYPE html>
<html lang="en">
<head>
<meta charset="utf-8">
<title>Marble Finch Co — Inform. Influence. Sell.</title>
<link href="https://fonts.googleapis.com/css2?family=Montserrat:wght@400;500;600;700;800&display=swap" rel="stylesheet">
<style>
:root{
  --blue:#1a86e0;
  --blue-deep:#0b3d91;
  --teal:#079a7c;
  --navy:#0f2646;
  --ink:#1b2230;
  --text:#333a46;
  --muted:#7b8394;
  --light:#eef0f6;
  --footer-bar:#e9ecf5;
  --white:#ffffff;
}
*{margin:0;padding:0;box-sizing:border-box}
html,body{width:1200px;height:3728px;overflow:hidden}
body{font-family:"Montserrat",sans-serif;color:var(--text);background:var(--white);position:relative}
section,header,footer{position:absolute;left:0;width:1200px}
.abs{position:absolute}

/* Hero */
.hero{top:0;height:697px;overflow:hidden}
.hero-photo{position:absolute;inset:0;background:
  radial-gradient(ellipse at 72% 22%,rgba(120,150,190,.55),transparent 45%),
  radial-gradient(ellipse at 30% 80%,rgba(120,70,40,.6),transparent 55%),
  linear-gradient(180deg,#2b2724 0%,#3a2d25 55%,#4a3528 100%)}
.hero-shade{position:absolute;inset:0;background:linear-gradient(90deg,rgba(10,12,20,.55),rgba(10,12,20,.1) 70%)}
.site-nav{position:absolute;top:0;left:0;width:1200px;height:70px;border-bottom:1px solid rgba(255,255,255,.18)}
.brand{position:absolute;left:137px;top:20px;color:var(--white);font-size:22px;font-weight:500;letter-spacing:.5px}
.nav-link{position:absolute;top:25px;color:var(--white);font-size:13px;font-weight:500;letter-spacing:.3px;text-decoration:none}
.nav-link.active{color:var(--blue)}
.nav-active-bar{position:absolute;left:437px;top:66px;width:50px;height:3px;background:var(--blue)}
.hero-rule{position:absolute;left:132px;top:229px;width:3px;height:138px;background:var(--white)}
.hero-kicker{position:absolute;left:147px;top:226px;color:var(--white);font-size:19px;font-weight:500}
.hero-title{position:absolute;left:146px;top:252px;color:var(--white);font-size:61px;font-weight:800;line-height:58px;letter-spacing:.5px}
.btn{display:inline-flex;align-items:center;justify-content:center;font-size:12px;font-weight:700;letter-spacing:.6px;color:var(--white);text-decoration:none}
.hero-btn{position:absolute;left:143px;top:392px;width:154px;height:39px;background:var(--blue)}
.scroll-cue{position:absolute;left:588px;top:630px}

/* Challenge */
.challenge{top:697px;height:579px}
.challenge-photo{position:absolute;left:123px;top:83px;width:521px;height:427px;background:
  radial-gradient(circle at 35% 48%,rgba(60,150,255,.55),transparent 40%),
  radial-gradient(circle at 70% 35%,rgba(60,150,255,.35),transparent 35%),
  linear-gradient(135deg,#071634,#0b2655 55%,#050d22)}
.dots{position:absolute;left:883px;top:299px}
.challenge-card{position:absolute;left:573px;top:123px;width:491px;height:338px;background:var(--white);box-shadow:0 10px 40px rgba(20,40,80,.12);padding:44px 55px 0 56px}
.section-title{font-size:29px;font-weight:500;color:var(--ink);line-height:1.1}
.section-title strong{font-weight:700;color:var(--blue)}
.title-bar{width:52px;height:3px;background:var(--blue);margin-top:12px}
.challenge-card p{font-size:13.5px;line-height:21.7px;color:var(--text);margin-top:4px}
.challenge-card .title-bar{margin-bottom:14px}
.pill-btn{position:absolute;left:59px;top:257px;width:139px;height:36px;border-radius:18px;background:linear-gradient(90deg,#1a6fd0,#2a8ee6)}

/* Help */
.help{top:1276px;height:573px;background:var(--light);overflow:hidden}
.help-photo{position:absolute;left:547px;top:0;width:653px;height:573px;background:
  radial-gradient(ellipse at 75% 45%,rgba(40,140,255,.9),transparent 55%),
  linear-gradient(90deg,rgba(238,240,246,1) 0%,rgba(120,150,200,.6) 25%,#123a8a 55%,#0a2466 100%)}
.kicker{font-size:15px;font-weight:500;color:var(--blue-deep);letter-spacing:.3px}
.help-copy{position:absolute;left:135px;top:128px;width:420px}
.help-copy .kicker{color:var(--blue-deep)}
.help-copy .section-title{font-size:32px;margin-top:6px}
.help-copy p{font-size:15px;line-height:23px;color:var(--text);margin-top:6px}
.help-copy .title-bar{margin-bottom:34px;width:62px}

/* Expertise */
.expertise{top:1849px;height:637px;background:linear-gradient(115deg,var(--blue-deep) 0%,#0d58a8 45%,#0b7f9a 75%,var(--teal) 100%);color:var(--white)}
.center-head{position:absolute;left:0;width:1200px;text-align:center}
.expertise .kicker{color:var(--white)}
.expertise .section-title{color:var(--white);font-size:32px;margin-top:8px}
.expertise .section-title strong{color:var(--white)}
.center-bar{width:62px;height:3px;background:var(--blue);margin:14px auto 0}
.service{position:absolute;width:213px;height:150px;border:1px solid rgba(255,255,255,.28);display:flex;flex-direction:column;align-items:center;justify-content:center;text-align:center;font-size:14.5px;font-weight:600;line-height:18px;color:var(--white)}
.service.featured{border:2px solid var(--white)}
.service svg{margin-bottom:12px}

/* Clients */
.clients{top:2486px;height:347px}
.clients .section-title{font-size:32px}
.client{position:absolute;top:2689px;transform:translateX(-50%);display:flex;align-items:center;gap:7px;font-size:15px;font-weight:600;color:var(--ink);white-space:nowrap}
.client i{display:block;width:12px;height:12px;border-radius:50%;background:var(--blue)}
.arrow{position:absolute;top:2692px}

/* Results */
.results{top:2833px;height:559px;background:linear-gradient(100deg,#102848 0%,#123c78 45%,#1a5fc0 80%,#2272d8 100%);overflow:hidden;color:var(--white)}
.results-photo{position:absolute;left:0;top:0}
.results-copy{position:absolute;left:139px;top:128px;width:420px}
.results-copy .section-title{color:var(--white);font-size:32px}
.results-copy .section-title strong{color:var(--white)}
.results-copy .title-bar{width:70px;margin-bottom:22px}
.results-copy p{font-size:16.5px;line-height:26px;padding-left:7px;margin-bottom:7px}
.outline-btn{position:absolute;left:149px;top:388px;width:142px;height:38px;border:2px solid var(--white);border-radius:19px}

/* Footer */
.site-footer{top:3392px;height:336px;background:var(--white)}
.footer-rule{position:absolute;top:0;width:1px;height:276px;background:#e3e6ee}
.footer-brand{position:absolute;left:153px;top:74px;font-size:24px;font-weight:500;color:var(--blue-deep);letter-spacing:.5px}
.footer-about{position:absolute;left:154px;top:116px;width:260px;font-size:10px;line-height:14px;color:var(--muted)}
.footer-col{position:absolute;top:76px}
.footer-col h4{font-size:13px;font-weight:700;color:var(--blue-deep);letter-spacing:.4px;margin-bottom:18px}
.footer-col a{display:block;font-size:11.5px;color:var(--text);text-decoration:none;margin-bottom:14px}
.col-mark{position:absolute;top:76px;width:3px;height:22px;background:var(--blue)}
.social{display:grid;grid-template-columns:auto auto;gap:8px 12px}
.social span{display:flex;align-items:center;gap:5px;font-size:11px;font-weight:600;color:var(--blue-deep)}
.social i{display:block;width:10px;height:10px;border-radius:50%;background:var(--blue)}
.legal{position:absolute;left:0;top:276px;width:1200px;height:60px;background:var(--footer-bar);text-align:center;line-height:60px;font-size:11px;color:var(--text)}
</style>
</head>
<body>

<header class="hero">
  <div class="hero-photo" role="img" aria-label="Photo of a speaker presenting on stage to a seated audience"></div>
  <div class="hero-shade"></div>
  <nav class="site-nav">
    <div class="brand">MARBLE FINCH CO</div>
    <a class="nav-link active" style="left:441px" href="#">HOME</a>
    <a class="nav-link" style="left:553px" href="#">ABOUT US</a>
    <a class="nav-link" style="left:695px" href="#">TESTIMONIALS</a>
    <a class="nav-link" style="left:864px" href="#">TEAM</a>
    <a class="nav-link" style="left:971px" href="#">CONTACT</a>
    <span class="nav-active-bar"></span>
  </nav>
  <span class="hero-rule"></span>
  <div class="hero-kicker">WELCOME TO MARBLE FINCH CO</div>
  <h1 class="hero-title">INFORM.<br>INFLUENCE. SELL.</h1>
  <a class="btn hero-btn" href="#">LEARN MORE</a>
  <svg class="scroll-cue" width="22" height="46" viewBox="0 0 22 46" fill="none" stroke="#fff" stroke-width="1.6">
    <rect x="3" y="1" width="16" height="26" rx="8"/>
    <line x1="11" y1="7" x2="11" y2="12"/>
    <polyline points="6,32 11,37 16,32"/>
    <polyline points="6,38 11,43 16,38"/>
  </svg>
</header>

<section class="challenge">
  <div class="challenge-photo" role="img" aria-label="Illustration of glowing hexagon icons labelled training, development and skills"></div>
  <svg class="dots" width="206" height="188" viewBox="0 0 206 188">
    <defs><pattern id="dotgrid" width="9" height="9" patternUnits="userSpaceOnUse"><circle cx="2" cy="2" r="1.3" fill="#5b8fe0"/></pattern></defs>
    <rect x="176" y="0" width="30" height="188" fill="url(#dotgrid)"/>
    <rect x="0" y="158" width="206" height="30" fill="url(#dotgrid)"/>
  </svg>
  <div class="challenge-card">
    <h2 class="section-title">THE BIG <strong>CHALLENGE</strong></h2>
    <div class="title-bar"></div>
    <p>In today’s competitive business environment, effective communication is more essential than ever before. It is the foundation upon which companies are built, careers are propelled, and knowledge is imparted.</p>
    <p>Effective communication is critical - without it, misunder-standings arise, errors occur, and business goals</p>
    <a class="btn pill-btn" href="#">LEARN MORE</a>
  </div>
</section>

<section class="help">
  <div class="help-photo" role="img" aria-label="Photo of a thoughtful woman in glasses blended with a night city skyline and digital icons"></div>
  <div class="help-copy">
    <div class="kicker">WHY WE ARE</div>
    <h2 class="section-title">HOW CAN <strong>WE HELP</strong></h2>
    <div class="title-bar"></div>
    <p>At Marble Finch Co, we help individuals and organiza-tions “get what they want” through clear and persua-sive communication.</p>
    <p>Our consulting, coaching, and training services help cli-ents achieve targeted business objectives, with an em-phasis on informing, influencing, and selling.</p>
  </div>
</section>

<section class="expertise">
  <div class="center-head" style="top:66px">
    <div class="kicker">WHAT WE DO</div>
    <h2 class="section-title">OUR <strong>EXPERTISE</strong></h2>
    <div class="center-bar"></div>
  </div>

  <div class="service featured" style="left:164px;top:184px">
    <svg width="50" height="46" viewBox="0 0 50 46" fill="none" stroke="#fff" stroke-width="1.5"><rect x="18" y="3" width="28" height="18"/><line x1="22" y1="9" x2="40" y2="9"/><line x1="22" y1="14" x2="36" y2="14"/><circle cx="9" cy="8" r="4"/><path d="M3 30v-10h12v10"/><circle cx="22" cy="32" r="3"/><circle cx="32" cy="32" r="3"/><circle cx="42" cy="32" r="3"/><path d="M17 43a5 5 0 0 1 10 0M27 43a5 5 0 0 1 10 0M37 43a5 5 0 0 1 10 0"/></svg>
    Sales Training
  </div>
  <div class="service" style="left:389px;top:184px">
    <svg width="50" height="46" viewBox="0 0 50 46" fill="none" stroke="#fff" stroke-width="1.5"><circle cx="25" cy="23" r="7"/><circle cx="25" cy="5" r="3"/><circle cx="25" cy="41" r="3"/><circle cx="7" cy="14" r="3"/><circle cx="43" cy="14" r="3"/><circle cx="7" cy="32" r="3"/><circle cx="43" cy="32" r="3"/><path d="M25 8v8M25 30v8M10 15l9 4M40 15l-9 4M10 31l9-4M40 31l-9-4"/></svg>
    Marketing Collateral
  </div>
  <div class="service" style="left:611px;top:184px">
    <svg width="50" height="46" viewBox="0 0 50 46" fill="none" stroke="#fff" stroke-width="1.5"><rect x="5" y="4" width="32" height="22"/><line x1="10" y1="11" x2="30" y2="11"/><line x1="10" y1="17" x2="24" y2="17"/><circle cx="37" cy="28" r="5"/><path d="M28 44v-6a9 9 0 0 1 18 0v6"/></svg>
    Presentation Skills<br>Training
  </div>
  <div class="service" style="left:831px;top:184px">
    <svg width="50" height="46" viewBox="0 0 50 46" fill="none" stroke="#fff" stroke-width="1.5"><rect x="8" y="4" width="34" height="26"/><line x1="8" y1="10" x2="42" y2="10"/><rect x="13" y="14" width="12" height="10"/><line x1="29" y1="16" x2="37" y2="16"/><line x1="29" y1="21" x2="37" y2="21"/><path d="M20 30v6h10v-6M14 40h22"/></svg>
    Corporate &amp; Website<br>Messaging
  </div>
  <div class="service" style="left:164px;top:346px">
    <svg width="50" height="46" viewBox="0 0 50 46" fill="none" stroke="#fff" stroke-width="1.5"><path d="M4 6h28v18H16l-7 6v-6H4z"/><line x1="9" y1="12" x2="27" y2="12"/><line x1="9" y1="18" x2="22" y2="18"/><path d="M36 16h10v18h-4v6l-7-6H22v-6"/></svg>
    Keynote Speeches
  </div>
  <div class="service" style="left:389px;top:346px">
    <svg width="50" height="46" viewBox="0 0 50 46" fill="none" stroke="#fff" stroke-width="1.5"><path d="M16 42v-9c-6-4-8-10-6-17 3-9 15-13 24-8 8 5 9 14 5 20l3 6-4 1v5h-8v2"/><circle cx="25" cy="19" r="5"/><path d="M25 10v4M25 24v4M16 19h4M30 19h4"/></svg>
    Elevator Pitches
  </div>
  <div class="service" style="left:611px;top:346px">
    <svg width="50" height="46" viewBox="0 0 50 46" fill="none" stroke="#fff" stroke-width="1.5"><rect x="20" y="4" width="18" height="38"/><rect x="38" y="14" width="8" height="28"/><path d="M24 10h4M32 10h2M24 16h4M32 16h2M24 22h4M32 22h2M24 28h4M32 28h2"/><circle cx="11" cy="32" r="8"/><path d="M11 28v8M9 30h4M9 34h4"/></svg>
    Venture Capital<br>Presentations &amp; Decks
  </div>
  <div class="service" style="left:831px;top:346px">
    <svg width="50" height="46" viewBox="0 0 50 46" fill="none" stroke="#fff" stroke-width="1.5"><path d="M4 4h30v20H18l-6 6v-6H4z"/><path d="M16 14h30v20h-8v6l-6-6H16z" fill="rgba(255,255,255,.08)"/><line x1="21" y1="20" x2="41" y2="20"/><line x1="21" y1="25" x2="41" y2="25"/><line x1="21" y1="30" x2="34" y2="30"/></svg>
    Convention &amp; Trade<br>Show Messaging
  </div>
</section>

<section class="clients">
  <div class="center-head" style="top:62px">
    <h2 class="section-title">OUR <strong>CLIENTS</strong></h2>
    <div class="center-bar"></div>
  </div>
</section>
<svg class="arrow" style="left:88px" width="32" height="20" viewBox="0 0 32 20" fill="none" stroke="#8aa0c0" stroke-width="2"><polyline points="10,2 2,10 10,18"/><line x1="2" y1="10" x2="31" y2="10"/></svg>
<div class="client" style="left:194px"><i></i>Orchard Labs</div>
<div class="client" style="left:350px"><i></i>Telvana</div>
<div class="client" style="left:517px"><i></i>Indigo Stage Troupe</div>
<div class="client" style="left:682px"><i></i>Harbor Piers Club</div>
<div class="client" style="left:855px"><i></i>Netvia</div>
<div class="client" style="left:1022px"><i></i>Crestbank</div>
<svg class="arrow" style="left:1095px" width="32" height="20" viewBox="0 0 32 20" fill="none" stroke="#8aa0c0" stroke-width="2"><polyline points="22,2 30,10 22,18"/><line x1="1" y1="10" x2="30" y2="10"/></svg>

<section class="results">
  <svg class="results-photo" width="1200" height="559" viewBox="0 0 1200 559" role="img" aria-label="Photo of a hand touching a glowing digital bar chart with a rising arrow">
    <defs>
      <radialGradient id="resultsGlow" cx="0.6" cy="0.45" r="0.6">
        <stop offset="0" stop-color="#7fc8ff"/>
        <stop offset="0.45" stop-color="#2f86e8"/>
        <stop offset="1" stop-color="#1a4fa6" stop-opacity="0"/>
      </radialGradient>
    </defs>
    <circle cx="868" cy="278" r="286" fill="url(#resultsGlow)"/>
  </svg>
  <div class="results-copy">
    <h2 class="section-title">THE <strong>RESULTS</strong></h2>
    <div class="title-bar"></div>
    <p>Whatever the message, and whatever the medium, we help clients establish a connection, make an im-pression, and drive audiences toward a predeter-mined course of action.</p>
    <p>This results in clear messaging, captivated audi-ences, and increased sales.</p>
  </div>
  <a class="btn outline-btn" href="#">LEARN MORE</a>
</section>

<footer class="site-footer">
  <span class="footer-rule" style="left:457px"></span>
  <span class="footer-rule" style="left:689px"></span>
  <span class="footer-rule" style="left:912px"></span>
  <div class="footer-brand">MARBLE FINCH CO</div>
  <p class="footer-about">Marble Finch Co partners with brands to maximize their message impact by providing clear, scalable and precision communication services.</p>

  <span class="col-mark" style="left:457px"></span>
  <div class="footer-col" style="left:504px">
    <h4>NAVIGATION</h4>
    <a href="#">Home</a><a href="#">About Us</a><a href="#">Our Services</a>
  </div>
  <span class="col-mark" style="left:689px"></span>
  <div class="footer-col" style="left:737px">
    <h4>RESOURCES</h4>
    <a href="#">Testimonials</a><a href="#">Team</a><a href="#">Contact Us</a>
  </div>
  <span class="col-mark" style="left:912px"></span>
  <div class="footer-col" style="left:930px">
    <h4>FOLLOW US</h4>
    <div class="social">
      <span><i></i>Linkly</span><span><i></i>Quipper</span>
      <span><i></i>Reelhub</span><span><i></i>Pixfeed</span>
    </div>
  </div>
  <div class="legal">© 2022 Marble Finch Co | All Rights Reserved</div>
</footer>

</body>
</html>
```